Brightmoor Partners Branding Revamp

We are a consulting company, looking for a way to display and promote our brand. We have 2 sides to the business- Brightmoor (financial) and Partners (cyber security). The financial side products relate to business necessities: card processing, website design/hosting/maintenance, VoIP phone systems. The cyber security side promotes a bundled package of 4 solutions: network vulnerability scan, dark web scan, anti-ransomeware/malware software, and image-level backups. We want people to understand that partnering with Brightmoor Partners gives them “Elevated Peace of Mind” (tagline). Current badge and logos uploaded.

Target Market(s)

Small businesses

Contact Information for Business Card

Lena Marwick, Vice President, lena@brightmoorpartners.example, 555-806-1937, www.brightmoorpartners.example

Requirements
Nice to have
• I do prefer the darker background for front and back

```html
<!DOCTYPE html>
<html lang="en">
<head>
<meta charset="utf-8">
<title>Brightmoor Partners – Business Cards</title>
<link rel="stylesheet" href="https://fonts.googleapis.com/css2?family=Arimo:wght@400;700&display=swap">
<style>
  :root {
    --backdrop: #c6c6c6;
    --maroon: #560002;
    --red-deep: #7e1117;
    --red: #c8181f;
    --red-bright: #ec1c24;
    --white: #ffffff;
  }
  * { box-sizing: border-box; margin: 0; padding: 0; }
  html, body { width: 1200px; height: 800px; overflow: hidden; }
  body {
    background: var(--backdrop);
    font-family: "Arimo", Arial, sans-serif;
    position: relative;
  }
  .card {
    position: absolute;
    top: 260px;
    width: 490px;
    height: 280px;
    overflow: hidden;
    box-shadow: 0 2px 6px rgba(0,0,0,0.18);
  }
  /* Back of card */
  .card--back {
    left: 75px;
    background: var(--maroon);
    display: flex;
    align-items: center;
    justify-content: center;
  }
  .brand-lockup {
    display: flex;
    align-items: center;
    gap: 14px;
  }
  .brand-lockup__square {
    width: 26px;
    height: 26px;
    background: var(--red-bright);
  }
  .brand-lockup__name {
    color: var(--white);
    font-weight: 700;
    font-size: 22px;
    letter-spacing: 0.22em;
    text-transform: uppercase;
  }
  /* Front of card */
  .card--front { left: 635px; background: var(--white); }
  .card__facets { position: absolute; inset: 0; width: 100%; height: 100%; }
  .front-brand {
    position: absolute;
    left: 22px;
    top: 98px;
    width: 120px;
    display: flex;
    flex-direction: column;
    align-items: flex-start;
    gap: 10px;
  }
  .front-brand__square { width: 22px; height: 22px; background: var(--red-bright); }
  .front-brand__name {
    color: var(--red);
    font-weight: 700;
    font-size: 13px;
    letter-spacing: 0.12em;
    text-transform: uppercase;
    line-height: 1.35;
  }
  .holder {
    position: absolute;
    left: 232px;
    top: 96px;
    color: var(--white);
  }
  .holder__name {
    font-weight: 400;
    font-size: 17px;
    letter-spacing: 0.06em;
    text-transform: uppercase;
  }
  .holder__title { font-size: 13px; margin-top: 3px; }
  .contact-list {
    position: absolute;
    left: 232px;
    top: 168px;
    list-style: none;
    color: var(--white);
    font-size: 14px;
  }
  .contact-list__item {
    display: flex;
    align-items: center;
    gap: 10px;
    height: 24px;
  }
  .contact-list__icon { width: 14px; height: 14px; flex: none; }
</style>
</head>
<body>

<section class="card card--back" aria-label="Business card back">
  <div class="brand-lockup">
    <span class="brand-lockup__square"></span>
    <span class="brand-lockup__name">Brightmoor Partners</span>
  </div>
</section>

<section class="card card--front" aria-label="Business card front">
  <svg class="card__facets" viewBox="0 0 490 280" preserveAspectRatio="none" aria-hidden="true">
    <defs>
      <linearGradient id="redField" x1="0" y1="0" x2="1" y2="1">
        <stop offset="0" stop-color="#7e1117"/>
        <stop offset="0.55" stop-color="#c8181f"/>
        <stop offset="1" stop-color="#a3161c"/>
      </linearGradient>
    </defs>
    <polygon points="165,0 490,0 490,280 205,280 195,190" fill="url(#redField)"/>
    <polygon points="195,190 205,280 150,280 120,232" fill="#ec1c24"/>
    <polygon points="330,0 490,0 490,150" fill="#ffffff" opacity="0.06"/>
    <polygon points="490,170 490,280 360,280" fill="#000000" opacity="0.12"/>
    <polygon points="205,280 260,200 340,280" fill="#ffffff" opacity="0.05"/>
  </svg>

  <div class="front-brand">
    <span class="front-brand__square"></span>
    <span class="front-brand__name">Brightmoor<br>Partners</span>
  </div>

  <div class="holder">
    <p class="holder__name">Lena Marwick</p>
    <p class="holder__title">Vice President</p>
  </div>

  <ul class="contact-list">
    <li class="contact-list__item">
      <svg class="contact-list__icon" viewBox="0 0 14 14" aria-hidden="true">
        <rect width="14" height="14" rx="2" fill="#fff"/>
        <path d="M4 3.5c.6 2.9 2.6 5.4 5.6 6.8l1-1.2-1.5-1-0.8.7c-1-.5-2-1.6-2.4-2.6l.7-.8-1-1.5z" fill="#c8181f"/>
      </svg>
      <span>555-806-1937</span>
    </li>
    <li class="contact-list__item">
      <svg class="contact-list__icon" viewBox="0 0 14 14" aria-hidden="true">
        <rect width="14" height="14" rx="2" fill="#fff"/>
        <path d="M3 4.5h8v5H3z M3 4.5l4 3 4-3" fill="none" stroke="#c8181f" stroke-width="1.1"/>
      </svg>
      <span>lena@brightmoorpartners.example</span>
    </li>
    <li class="contact-list__item">
      <svg class="contact-list__icon" viewBox="0 0 14 14" aria-hidden="true">
        <circle cx="7" cy="7" r="6.5" fill="#fff"/>
        <path d="M1 7h12M7 1c-2.2 2-2.2 10 0 12M7 1c2.2 2 2.2 10 0 12" fill="none" stroke="#c8181f" stroke-width="0.9"/>
      </svg>
      <span>www.brightmoorpartners.example</span>
    </li>
  </ul>
</section>

</body>
</html>
```